Web Design for an Innovative Life Science Marketplace

IMPORTANT:
The software is called CS-Cart. It has capabilities and limitations with design features in the software. There is a certain framework that needs to be followed. It is PHP and Linux. It may require add-ons for your design, so please be specific with what is required. It’s preferred the designer has CS-Cart knowledge/experience.

Key Requirements
1. I’d like the design to include an implemented/recommended CS-Cart theme that is consistent with our branding (see the marketing collateral and logo).
2. I then need the additional design changes to that theme to create the below web pages.
3. All designs should be consistent with our branding. All pictures should either be computer generated (clip art-like) or pictures of happy patients. What is a happy patient? Close up photo of someone healthy, happy, and experiencing/enjoying life. Not someone in a hospital or getting care. Please see examples already on the site.

Please see the attached Web Design details in the word document. That document is important to complete the design.

```html
<!DOCTYPE html>
<html lang="en">
<head>
<meta charset="utf-8">
<title>CircuLab – Life Science Marketplace</title>
<link rel="stylesheet" href="https://fonts.googleapis.com/css2?family=Montserrat:wght@400;600;700;800&family=Open+Sans:wght@400;600;700&display=swap">
<style>
:root{
  --lime:#8cc63f;
  --lime-dark:#6fae2a;
  --teal:#22876b;
  --teal-deep:#155446;
  --forest:#1d5e4c;
  --ink:#3a3a3a;
  --muted:#6b6b6b;
  --paper:#ffffff;
  --mist:#f2f5f1;
}
*{box-sizing:border-box;margin:0;padding:0}
html,body{width:1200px;height:3804px;overflow:hidden}
body{position:relative;background:var(--paper);font-family:'Open Sans',sans-serif;color:var(--ink)}
.abs{position:absolute}
.btn{display:inline-block;background:var(--lime);color:#fff;font-family:'Montserrat',sans-serif;font-weight:700;font-size:20px;letter-spacing:.5px;border-radius:30px;padding:14px 34px;text-transform:uppercase}
.brand{display:flex;align-items:center;gap:12px;font-family:'Montserrat',sans-serif;font-weight:800;font-size:30px;color:var(--lime-dark)}
.brand-dot{width:56px;height:56px;border-radius:50%;border:4px solid var(--lime);background:#fff}

/* header */
.site-header{top:0;left:0;width:1200px;height:160px;background:#fff}
.utility{top:10px;right:40px;display:flex;gap:30px;font-size:15px;font-family:'Montserrat',sans-serif;font-weight:600;color:var(--forest)}
.utility span{display:flex;align-items:center;gap:8px}
.utility i{width:14px;height:14px;border-radius:3px;background:var(--lime)}
.site-header .brand{left:70px;top:44px}
.main-nav{left:370px;top:62px;display:flex;gap:28px;align-items:center;font-family:'Montserrat',sans-serif;font-weight:700;font-size:15px;color:var(--forest)}
.main-nav .active{background:var(--lime);color:#fff;padding:10px 22px;border-radius:20px}

/* hero */
.hero{top:160px;left:0;width:1200px;height:560px;background:linear-gradient(90deg,#bfcab5 0%,#d9dccf 40%,#e9d3bd 70%,#c8b195 100%)}
.hero-title{left:80px;top:70px;font-family:'Montserrat',sans-serif;font-weight:800;font-size:46px;color:#fff;text-shadow:0 2px 6px rgba(0,0,0,.25)}
.hero-text{left:80px;top:130px;width:470px;font-size:15px;color:#fff;line-height:1.45;text-shadow:0 1px 3px rgba(0,0,0,.3)}
.hero-actions{left:80px;top:280px;display:flex;gap:18px}
.hero-arrow{top:180px;width:44px;height:44px;border-radius:50%;background:rgba(255,255,255,.6)}
.hero-wave{top:560px;left:0}
.feature{top:600px;width:300px;text-align:center}
.feature-icon{margin:0 auto;width:118px;height:118px;border-radius:50%;background:#fff;border:5px solid var(--lime);display:flex;align-items:center;justify-content:center}
.feature h3{margin-top:22px;font-family:'Montserrat',sans-serif;font-weight:700;font-size:22px;color:var(--teal);text-transform:uppercase}
.feature p{margin-top:6px;font-size:14px;color:var(--muted);line-height:1.4}

/* welcome */
.welcome{top:940px;left:0;width:1200px;height:520px;background:linear-gradient(180deg,#2f7a5f 0%,#1d5e4c 55%,#2a6f55 100%);text-align:center;color:#fff}
.welcome h2{margin-top:58px;font-family:'Montserrat',sans-serif;font-weight:700;font-size:42px;letter-spacing:1px}
.welcome p{width:920px;margin:18px auto 0;font-size:15px;line-height:1.6}
.welcome .btn{margin-top:48px}

/* products */
.section-title{font-family:'Montserrat',sans-serif;font-weight:800;font-size:46px;color:var(--teal)}
.products-title{left:80px;top:1520px}
.products-sub{left:80px;top:1582px;width:420px;font-size:14px;color:var(--muted);line-height:1.45}
.product{width:260px;height:220px;overflow:hidden;box-shadow:0 6px 14px rgba(0,0,0,.15)}
.product .ph{position:absolute;inset:0}
.product .label{position:absolute;left:0;right:0;bottom:0;background:rgba(255,255,255,.92);padding:12px;text-align:center;font-family:'Montserrat',sans-serif;font-weight:700;font-size:18px;color:var(--teal);text-transform:uppercase}
.product.raw .label{top:0;bottom:0;background:rgba(34,135,107,.82);color:#fff;text-align:center;padding-top:60px}
.product.raw .label small{display:block;margin-top:8px;font-family:'Open Sans',sans-serif;font-weight:400;font-size:13px;text-transform:none;line-height:1.4}

/* promise */
.promise{top:2080px;left:0;width:1200px;height:660px;background:linear-gradient(120deg,#4f7a3a 0%,#9bb36d 35%,#e7d9be 60%,#b9c78f 100%)}
.promise-card{left:752px;top:2460px;width:408px;height:220px;background:#fff;padding:30px 36px}
.promise-card h2{font-family:'Montserrat',sans-serif;font-weight:800;font-size:36px;color:var(--teal)}
.promise-card p{margin-top:12px;font-size:17px;color:var(--muted);line-height:1.45}

/* resources */
.resource{top:2730px;width:500px}
.resource h2{font-family:'Montserrat',sans-serif;font-weight:800;font-size:44px;color:var(--lime-dark)}
.resource .ph{margin-top:16px;width:460px;height:200px}
.resource p{margin-top:14px;width:420px;font-size:15px;color:var(--ink);line-height:1.45}
.resource .btn{margin-top:24px;font-size:16px;padding:12px 30px}

/* footer */
.footer-wave{top:3200px;left:0}
.footer-badge{top:3228px;left:540px;width:120px;height:120px;border-radius:50%;background:#fff;border:5px solid var(--lime);display:flex;align-items:center;justify-content:center;font-family:'Montserrat',sans-serif;font-weight:800;font-size:18px;color:var(--lime-dark)}
.site-footer{top:3340px;left:0;width:1200px;height:400px;background:var(--forest);color:#fff}
.site-footer h4{font-family:'Montserrat',sans-serif;font-weight:700;font-size:20px;text-transform:uppercase;margin-bottom:16px}
.col-contact{left:80px;top:20px;width:380px}
.field{height:34px;background:#fff;border-radius:3px;margin-bottom:12px;padding:7px 12px;font-size:14px;color:#888}
.field.tall{height:70px}
.col-contact .btn{font-size:16px;padding:10px 30px}
.col-info{left:560px;top:20px;width:300px;font-size:14px;line-height:1.5}
.info-row{display:flex;gap:12px;margin-bottom:14px}
.info-row svg{flex:none;margin-top:3px}
.social{display:flex;gap:12px;margin-top:6px}
.social span{width:40px;height:40px;border-radius:50%;background:var(--lime)}
.col-map{left:900px;top:20px;font-size:14px;line-height:2}
.col-map li{list-style:none;padding-left:16px;position:relative}
.col-map li:before{content:"";position:absolute;left:0;top:12px;width:6px;height:6px;background:var(--lime);border-radius:50%}
.footer-bar{top:3740px;left:0;width:1200px;height:64px;background:var(--lime);color:#fff;text-align:center;font-size:14px;line-height:64px}
</style>
</head>
<body>

<header class="site-header abs">
  <div class="utility abs"><span><i></i>QUALITY POLICY</span><span><i></i>My Account</span><span><i></i>My Cart</span></div>
  <div class="brand abs"><span class="brand-dot"></span>CIRCULAB</div>
  <nav class="main-nav abs">
    <span class="active">HOME</span><span>WHY CIRCULAB?</span><span>ABOUT US</span><span>OUR PARTNERS</span><span>WHITE PAPER</span><span>CONTACT US</span>
  </nav>
</header>

<section class="hero abs" role="img" aria-label="Close-up photo of a smiling, healthy young woman outdoors">
  <h1 class="hero-title abs">JOIN THE CIRCULAR<br>SUPPLY CHAIN</h1>
  <p class="hero-text abs" style="top:190px">A trusted online marketplace where life science buyers and sellers trade surplus materials and equipment.</p>
  <div class="hero-actions abs"><span class="btn">Pre-Register</span><span class="btn">Login</span></div>
  <span class="hero-arrow abs" style="left:16px"></span>
  <span class="hero-arrow abs" style="right:16px"></span>
</section>
<svg class="hero-wave abs" width="1200" height="160" viewBox="0 0 1200 160">
  <path d="M0 60 C300 150 900 150 1200 30 L1200 160 L0 160Z" fill="#fff"/>
  <path d="M0 60 C300 150 900 150 1200 30" fill="none" stroke="#8cc63f" stroke-width="6"/>
</svg>

<div class="feature abs" style="left:120px">
  <div class="feature-icon"><svg width="60" height="60" viewBox="0 0 60 60" fill="none" stroke="#22876b" stroke-width="3"><circle cx="30" cy="30" r="6"/><ellipse cx="30" cy="30" rx="24" ry="9"/><ellipse cx="30" cy="30" rx="24" ry="9" transform="rotate(60 30 30)"/><ellipse cx="30" cy="30" rx="24" ry="9" transform="rotate(-60 30 30)"/></svg></div>
  <h3>Manufacturers</h3>
  <p>Create an account in minutes to sell and buy surplus materials and equipment</p>
</div>
<div class="feature abs" style="left:450px">
  <div class="feature-icon"><svg width="60" height="60" viewBox="0 0 60 60" fill="none" stroke="#22876b" stroke-width="3"><circle cx="26" cy="26" r="14"/><path d="M36 36 L50 50"/></svg></div>
  <h3>Researchers</h3>
  <p>Source low-cost materials and reduce lab expenses</p>
</div>
<div class="feature abs" style="left:780px">
  <div class="feature-icon"><svg width="60" height="60" viewBox="0 0 60 60" fill="none" stroke="#22876b" stroke-width="3"><path d="M14 50 V24 L30 12 L46 24 V50 Z"/><path d="M24 50 V34 H36 V50"/></svg></div>
  <h3>Original Suppliers</h3>
  <p>Market your products across a broad life sciences network</p>
</div>

<section class="welcome abs" role="img" aria-label="Green-tinted photo of a laboratory">
  <h2>WELCOME TO CIRCULAB</h2>
  <p>We are a private and virtual B2B marketplace and consortium for the life science manufacturers, researchers and vendors to sell, purchase and store surplus materials and equipment as well as collaborate on non-financial initiatives.</p>
  <p>We are in the developmental phase of our platform, working with some of the most trusted partners in the industry. We are tentatively scheduled for an exclusive launch during the year ahead.</p>
  <p>We aspire to transform the life science industry's purchasing of surplus and excess inventory to one that is sustainable, transparent and efficient, reducing waste and delivering real value to every member of our community.</p>
  <span class="btn">How It Work</span>
</section>

<h2 class="section-title products-title abs">OUR PRODUCTS</h2>
<p class="products-sub abs">How Pharma's Demand Volatility Could Be Costing You Millions in Materials Write-downs &amp; Procurement</p>

<div class="product raw abs" style="left:80px;top:1820px">
  <div class="ph" role="img" aria-label="Photo of raw laboratory materials" style="background:linear-gradient(135deg,#3f8f78,#8fbfae)"></div>
  <div class="label">Raw Materials<small>Consumables and reagents sourced from trusted members at fair prices.</small></div>
</div>
<div class="product abs" style="left:340px;top:1760px">
  <div class="ph" role="img" aria-label="Photo of laboratory equipment" style="background:linear-gradient(135deg,#e8ecef,#a9b8bf)"></div>
  <div class="label">Equipment</div>
</div>
<div class="product abs" style="left:600px;top:1672px">
  <div class="ph" role="img" aria-label="Photo of blue-lit machine parts" style="background:linear-gradient(135deg,#0c2f66,#2f79c9)"></div>
  <div class="label">Parts</div>
</div>
<div class="product abs" style="left:860px;top:1592px">
  <div class="ph" role="img" aria-label="Photo of business colleagues collaborating" style="background:linear-gradient(135deg,#d8dde2,#8f9aa6)"></div>
  <div class="label">Collaborative Relationships</div>
</div>

<section class="promise abs" role="img" aria-label="Photo of a laughing young woman lying in the grass"></section>
<div class="promise-card abs">
  <h2>OUR PROMISE</h2>
  <p>A greener, more cost-efficient, and quality-driven supply chain through a collaborative life sciences marketplace</p>
</div>

<div class="resource abs" style="left:80px">
  <h2>WHITE PAPER</h2>
  <div class="ph" role="img" aria-label="Photo of a hand writing on paper with a pen" style="background:linear-gradient(135deg,#f1f1ef,#b9bbb8)"></div>
  <p>How Pharma's Demand Volatility Could Be Costing You Millions in Materials Write-downs &amp; Procurement</p>
  <span class="btn">White Paper</span>
</div>
<div class="resource abs" style="left:610px">
  <h2>BROCHURE</h2>
  <div class="ph" role="img" aria-label="Photo of a smiling baby" style="background:linear-gradient(135deg,#cfe0ef,#f1e1d1)"></div>
  <p>How Pharma's Demand Volatility Could Be Costing You Millions in Materials Write-downs &amp; Procurement</p>
  <span class="btn">Brochure</span>
</div>

<svg class="footer-wave abs" width="1200" height="160" viewBox="0 0 1200 160">
  <path d="M0 100 C350 160 850 40 1200 110 L1200 160 L0 160Z" fill="#1d5e4c"/>
  <path d="M0 100 C350 160 850 40 1200 110" fill="none" stroke="#8cc63f" stroke-width="6"/>
</svg>
<div class="footer-badge abs">CIRCULAB</div>

<footer class="site-footer abs">
  <div class="col-contact abs">
    <h4>Contact Us</h4>
    <div class="field">Name *</div>
    <div class="field">Email *</div>
    <div class="field">Phone *</div>
    <div class="field tall">Message *</div>
    <span class="btn">Submit</span>
  </div>
  <div class="col-info abs">
    <h4>Contact Info</h4>
    <div class="info-row"><svg width="18" height="22" viewBox="0 0 18 22"><path d="M9 1C4.6 1 1 4.5 1 8.8 1 14.5 9 21 9 21s8-6.5 8-12.2C17 4.5 13.4 1 9 1z" fill="#8cc63f"/><circle cx="9" cy="9" r="3" fill="#1d5e4c"/></svg><span><b>CIRCULAB</b><br>200 Harbor Way, Suite 4<br>Riverton, PA 15000</span></div>
    <div class="info-row"><svg width="18" height="18" viewBox="0 0 18 18"><path d="M4 1l3 4-2 2c1 2 3 4 5 5l2-2 4 3-2 3C8 16 2 10 1 4z" fill="#8cc63f"/></svg><span>+1 (555) 014-2290</span></div>
    <div class="info-row"><svg width="18" height="14" viewBox="0 0 18 14"><rect x="1" y="1" width="16" height="12" fill="#8cc63f"/><path d="M1 1l8 7 8-7" fill="none" stroke="#1d5e4c" stroke-width="1.5"/></svg><span>hello@circulab.example</span></div>
    <div class="social"><span></span><span></span><span></span></div>
  </div>
  <div class="col-map abs">
    <h4>Sitemap</h4>
    <ul>
      <li>Home</li><li>About Us</li><li>How It Works</li><li>Our Partners</li><li>White Paper</li><li>Quality Policy</li><li>Privacy Policy</li><li>Contact Us</li>
    </ul>
  </div>
</footer>
<div class="footer-bar abs">© CIRCULAB · 2018 · All Rights Reserved.</div>

</body>
</html>
```